New Web Site Design - Ironwood Signal Solutions

We are looking for a completely new web site design. Ironwood Signal Solutions is a full service company providing PBX and IP/Cloud Based phone systems. We also sell and install video camera surveillance systems and provide low voltage cabling services (CAT5 and CAT3). We are looking for something professional looking. We want to be able to showcase our vendor partners as well as be able to show photos of some of the work we have done. We will also want to be able to post PDF brochures as well as make changes to the website ourselves.

Target Market(s)

Commercial

Industry/Entity Type

Communication

Coding

Coded - Design and coding required

Number of Pages Required

5+ page

Font styles to use
Sans Serif

Colors
0455a3

Requirements
Must have
• Ability to upload PDF brochures
• Professional look and feel
• Ability to upload and easily insert job photos
• Thinking it should have at least 6 pages: Main page, phone systems and services page, carrier services page, video surveillance systems and service page, low voltage cabling services page, contact us page

```html
<!DOCTYPE html>
<html lang="en">
<head>
<meta charset="utf-8">
<title>Ironwood Signal Solutions</title>
<link rel="stylesheet" href="https://fonts.googleapis.com/css2?family=Arimo:wght@400;700&family=Oswald:wght@200;300&display=swap">
<style>
:root{
  --navy:#0b3170;
  --ink:#333333;
  --muted:#6b6b7a;
  --topbar:#3b3b3b;
  --pale:#e8ebf0;
  --white:#ffffff;
  --sans:"Arimo", Arial, sans-serif;
}
*{box-sizing:border-box;margin:0;padding:0}
html,body{width:1200px;height:2667px;overflow:hidden;background:var(--white)}
body{font-family:var(--sans);color:var(--ink);position:relative}
a{color:inherit;text-decoration:none}

/* top bar */
.topbar{height:36px;background:var(--topbar);color:#eee;font-size:11px;display:flex;align-items:center;padding:0 78px}
.topbar .contact{display:flex;align-items:center;margin-right:40px;gap:8px}
.topbar .contact svg{width:12px;height:12px;fill:#fff}
.topbar .socials{margin-left:auto;display:flex;gap:18px}
.topbar .socials span{width:14px;height:14px;border-radius:50%;background:#777}

/* header */
.header{height:88px;display:flex;align-items:center;padding:0 78px;border-bottom:1px solid #eee}
.brand-name{font-size:21px;color:var(--navy);font-weight:400;line-height:1.15;white-space:nowrap}
.nav{margin-left:auto;display:flex;align-items:center;font-size:13px;color:#444}
.nav a{padding:0 27px;line-height:32px}
.nav a.active{background:var(--navy);color:#fff;padding:0 23px}
.nav a.has-sub{position:relative}
.nav a.has-sub::after{content:"";position:absolute;left:50%;bottom:-4px;width:4px;height:1px;background:var(--navy)}

/* hero */
.hero{position:relative;height:431px;background:radial-gradient(ellipse 70% 90% at 55% 95%,#3a8cc4 0%,#14507f 35%,#0a2440 65%,#040d1a 100%);display:flex;align-items:center;justify-content:center}
.hero h1{font-family:"Oswald",sans-serif;font-weight:200;font-size:100px;color:#fff;letter-spacing:1px;text-shadow:0 2px 4px rgba(0,0,0,.6)}
.hero .arrow{position:absolute;top:196px;width:43px;height:41px;background:rgba(220,220,220,.85);display:flex;align-items:center;justify-content:center}
.hero .arrow svg{width:16px;height:22px;stroke:#333;fill:none;stroke-width:2}
.hero .prev{left:57px}.hero .next{right:57px}

/* services */
.services{height:551px;background:var(--pale);display:flex;justify-content:center;gap:59px;padding-top:73px}
.service{width:208px;text-align:center}
.service .tile{width:208px;height:206px;background:var(--navy);display:flex;align-items:center;justify-content:center}
.service .tile svg{width:86px;height:86px;fill:#fff}
.service h2{font-size:28px;font-weight:700;margin:38px 0 16px;color:#2d2d2d}
.service p{font-size:13px;line-height:22px;color:#3c4a66}
.btn{display:inline-block;margin-top:26px;background:#fff;color:#333;font-size:12px;padding:11px 16px;border-radius:3px}

/* communicate */
.communicate{height:508px;text-align:center;padding-top:56px;position:relative}
.section-title{font-size:33px;font-weight:700;color:#2d2d2d}
.photo{margin:26px auto 0;width:712px;height:236px;background:linear-gradient(90deg,#e4ecf4 0%,#cfdbe6 40%,#c9a48e 70%,#e9eef3 100%)}
.slide-chev{position:absolute;top:253px;width:14px;height:20px;stroke:#bbb;fill:none;stroke-width:2}
.communicate p{margin:28px auto 0;width:680px;font-size:14px;line-height:22px;color:var(--muted)}

/* stats */
.stats{height:357px;text-align:center;padding-top:26px}
.stat-row{display:flex;justify-content:center;gap:30px;margin-top:30px}
.stat{width:240px}
.stat .num{font-size:64px;color:var(--navy);line-height:1}
.stat h3{font-size:15px;font-weight:400;margin:16px 0 16px;color:#222}
.stat p{font-size:12.5px;line-height:20px;color:var(--muted)}
.stat .go{width:32px;height:32px;border-radius:50%;background:var(--navy);margin:22px auto 0;display:flex;align-items:center;justify-content:center}
.stat .go svg{width:10px;height:12px;stroke:#fff;fill:none;stroke-width:2.5}

/* help */
.help{height:397px;background:linear-gradient(100deg,#b7c5d6 0%,#cdd8e5 35%,#a9bbd3 70%,#8fa6c4 100%);text-align:center;padding-top:60px}
.help h2{font-size:43px;font-weight:700;color:#fff;line-height:44px}
.help-row{display:flex;justify-content:center;gap:155px;margin-top:80px}
.help-item{width:110px;display:flex;flex-direction:column;align-items:center}
.help-item .box{width:110px;height:110px;background:rgba(255,255,255,.55);display:flex;align-items:center;justify-content:center}
.help-item .box svg{width:40px;height:40px;fill:#333}
.help-item span{margin-top:20px;font-size:16px;font-weight:700;color:#fff;white-space:nowrap}

/* footer */
.footer{height:249px;display:flex;align-items:flex-start;padding:58px 0 0 78px}
.footer-brand{width:260px;padding-top:10px}
.footer-brand .brand-name{font-size:18px}
.footer .socials{display:flex;gap:20px;margin-top:10px;width:272px}
.footer .socials span{width:17px;height:17px;border-radius:50%;background:#999}
.fcol{width:180px}
.fcol h4{font-size:16px;font-weight:700;margin-bottom:14px;color:#222}
.fcol li{list-style:none;font-size:11px;color:#888;line-height:28px}
.fcol li::before{content:"•";margin-right:8px}
</style>
</head>
<body>

<div class="topbar">
  <div class="contact"><svg viewBox="0 0 12 12"><path d="M6 0a4 4 0 0 0-4 4c0 3 4 8 4 8s4-5 4-8a4 4 0 0 0-4-4zm0 5.5A1.5 1.5 0 1 1 6 2.5a1.5 1.5 0 0 1 0 3z"/></svg>214 Harbor Lane, Millbrook, MB 12 Ln 8</div>
  <div class="contact"><svg viewBox="0 0 12 12"><path d="M0 2h12v8H0zM1 3v.4L6 7l5-3.6V3z" fill-rule="evenodd"/></svg>hello@ironwoodsignal.net</div>
  <div class="contact"><svg viewBox="0 0 12 12"><path d="M2 0l2.5 3-1.3 1.5a7 7 0 0 0 4.3 4.3L9 7.5l3 2.5-1.5 2C5 12 0 7 0 1.5z"/></svg>+1 800 555 0142</div>
  <div class="socials"><span></span><span></span><span></span><span></span><span></span></div>
</div>

<header class="header">
  <div class="brand-name">Ironwood Signal Solutions</div>
  <nav class="nav">
    <a class="active" href="#">Home</a>
    <a class="has-sub" href="#">About</a>
    <a href="#">Services</a>
    <a href="#">Projects</a>
    <a href="#">Blog</a>
    <a href="#">Contacts</a>
  </nav>
</header>

<section class="hero" role="img" aria-label="Glowing blue globe in space wrapped with network light lines">
  <a class="arrow prev" href="#"><svg viewBox="0 0 16 22"><path d="M12 2 3 11l9 9"/></svg></a>
  <h1>SPEED &amp; QUALITY</h1>
  <a class="arrow next" href="#"><svg viewBox="0 0 16 22"><path d="M4 2l9 9-9 9"/></svg></a>
</section>

<section class="services">
  <article class="service">
    <div class="tile"><svg viewBox="0 0 24 24"><path d="M9 6l1 2 2 .5 1.5-1.5 1.5 1.5-1 1.8.8 2 2 .2v2l-2 .3-.8 2 1.2 1.7-1.5 1.5-1.7-1.2-2 .8-.3 2H7.7l-.3-2-2-.8-1.7 1.2-1.5-1.5 1.2-1.7-.8-2-2-.3v-2l2-.2.8-2-1-1.8L3.5 7.5 5 9l2-.5 1-2.5zm-.3 6a2 2 0 1 0 0 4 2 2 0 0 0 0-4zM18 1l.6 1.2 1.3.2.4-1.1 1.3.7-.5 1.2.8 1 1.3-.2.3 1.4-1.2.4v1.3l1.2.5-.5 1.3-1.3-.3-.8.9.4 1.2-1.3.6-.6-1.1-1.3.1-.5 1.2-1.3-.5.3-1.3-1-.8-1.2.5-.6-1.3 1.1-.6V5.8L14 5.3l.5-1.3 1.3.3.9-.9-.3-1.3zm.3 3.5a1.5 1.5 0 1 0 0 3 1.5 1.5 0 0 0 0-3z"/></svg></div>
    <h2>Hardware</h2>
    <p>Lorem ipsum dolor sit amet, consectetur adipisicing elit, sed do eiusmod tempor incidid.</p>
    <a class="btn" href="#">Read More</a>
  </article>
  <article class="service">
    <div class="tile"><svg viewBox="0 0 24 24"><path d="M12 2a7 7 0 0 0-7 7v3h2V9a5 5 0 0 1 10 0v3h2V9a7 7 0 0 0-7-7zM4 10h2v5H4zm14 0h2v5h-2zM12 5a4 4 0 1 1 0 8 4 4 0 0 1 0-8zm-7 17c0-4 3-6 7-6s7 2 7 6z"/></svg></div>
    <h2>Networking</h2>
    <p>Lorem ipsum dolor sit amet, consectetur adipisicing elit, sed do eiusmod tempor incidid.</p>
    <a class="btn" href="#">Read More</a>
  </article>
  <article class="service">
    <div class="tile"><svg viewBox="0 0 24 24"><path d="M3 2h10v20H3zm1.5 2v14h7V4zM14 6h7v14h-7v-2h5.5V8H14zM7 9l-2 2 2 2v-1l-1-1 1-1zm2 0v1l1 1-1 1v1l2-2z"/></svg></div>
    <h2>Innovation</h2>
    <p>Lorem ipsum dolor sit amet, consectetur adipisicing elit, sed do eiusmod tempor incidid.</p>
    <a class="btn" href="#">Read More</a>
  </article>
  <article class="service">
    <div class="tile"><svg viewBox="0 0 24 24"><path d="M1 3h20v13h-7v-1.5h5.5v-10h-17v10H10V16H1zm3 3h12v1.5H4zm0 3h9v1.5H4zm9 2.5l2-.5v4l3-.5 3 2-1 5h-5l-2.5-4z"/></svg></div>
    <h2>Development</h2>
    <p>Lorem ipsum dolor sit amet, consectetur adipisicing elit, sed do eiusmod tempor incidid.</p>
    <a class="btn" href="#">Read More</a>
  </article>
</section>

<section class="communicate">
  <h2 class="section-title">Communicate With The World</h2>
  <svg class="slide-chev" style="left:222px" viewBox="0 0 14 20"><path d="M11 2 3 10l8 8"/></svg>
  <div class="photo" role="img" aria-label="Smiling woman using a tablet in a bright room"></div>
  <svg class="slide-chev" style="right:222px" viewBox="0 0 14 20"><path d="M3 2l8 8-8 8"/></svg>
  <p>At vero eos et accusamus et iusto odio dignissimos ducimus qui blanditiis praesentium voluptatum deleniti atque<br>corrupti quos dolores et quas molestias excepturi sint occaecati cupiditate non provident similique sunt in culpa qui officia</p>
</section>

<section class="stats">
  <h2 class="section-title">Innovative Ways</h2>
  <div class="stat-row">
    <div class="stat"><div class="num">80</div><h3>TEMPORIBUS AUTEM</h3><p>Lorem ipsum dolor sit amet, consectetur adipisicing elit, sed do eiusmod tempor incididunt ut labore</p><div class="go"><svg viewBox="0 0 10 12"><path d="M3 1l5 5-5 5"/></svg></div></div>
    <div class="stat"><div class="num">120</div><h3>ITAQUE EARUM</h3><p>Lorem ipsum dolor sit amet, consectetur adipisicing elit, sed do eiusmod tempor incididunt ut labore</p><div class="go"><svg viewBox="0 0 10 12"><path d="M3 1l5 5-5 5"/></svg></div></div>
    <div class="stat"><div class="num">75</div><h3>EXCEPTEUR SINT</h3><p>Lorem ipsum dolor sit amet, consectetur adipisicing elit, sed do eiusmod tempor incididunt ut labore</p><div class="go"><svg viewBox="0 0 10 12"><path d="M3 1l5 5-5 5"/></svg></div></div>
    <div class="stat"><div class="num">90</div><h3>DUIS AUTE IRURE</h3><p>Lorem ipsum dolor sit amet, consectetur adipisicing elit, sed do eiusmod tempor incididunt ut labore</p><div class="go"><svg viewBox="0 0 10 12"><path d="M3 1l5 5-5 5"/></svg></div></div>
  </div>
</section>

<section class="help" role="img" aria-label="Soft blurred office scene in pale blue tones">
  <h2>Just in case you<br>need any help</h2>
  <div class="help-row">
    <div class="help-item"><div class="box"><svg viewBox="0 0 24 24"><path d="M2 10l10-7 10 7v11H2zm2 1.5V19h16v-7.5l-8 5.5z"/></svg></div><span>EMAIL SUPPORT</span></div>
    <div class="help-item"><div class="box"><svg viewBox="0 0 24 24"><path d="M14 2a5 5 0 0 0-4.5 7L2 16.5 5.5 20l7.5-7.5A5 5 0 0 0 20 8l-3 3-3-1-1-3 3-3a5 5 0 0 0-2-2zM4 3l3 1 6 6-2 2-6-6zm11 11 2-2 5 5-2 4-1 0z"/></svg></div><span>24/7 SUPPORT</span></div>
    <div class="help-item"><div class="box"><svg viewBox="0 0 24 24"><path d="M8 1 1 8l15 15 7-7zm0 3 12 12-4 4L4 8z"/></svg></div><span>FREE PHONE</span></div>
    <div class="help-item"><div class="box"><svg viewBox="0 0 24 24"><path d="M12 2a10 10 0 1 0 0 20 10 10 0 0 0 0-20zm1 16h-2v-2h2zm2-7.5c-.9.9-2 1.4-2 3h-2c0-2.5 1.5-3 2.3-3.8.9-.9.4-2.7-1.3-2.7A1.8 1.8 0 0 0 10 9H8a4 4 0 0 1 8 0c0 .6-.3 1-1 1.5z"/></svg></div><span>FAQ</span></div>
  </div>
</section>

<footer class="footer">
  <div class="footer-brand"><div class="brand-name">Ironwood Signal Solutions</div></div>
  <div class="socials"><span></span><span></span><span></span><span></span><span></span></div>
  <div class="fcol"><h4>Important Links</h4><ul><li>Affiliate Program</li><li>Special Promotions</li><li>Newsletter</li><li>Contact</li></ul></div>
  <div class="fcol"><h4>Support Menu</h4><ul><li>Lost Password?</li><li>Forgot your Username?</li><li>Your Membership</li><li>Your Account</li><li>Support Forum</li></ul></div>
  <div class="fcol"><h4>About Us</h4><ul><li>Customer focus</li><li>Performance</li><li>Innovation</li><li>Responsibility</li></ul></div>
</footer>

</body>
</html>
```